Personal Business Card

Looking for a clean and modern personal business card. Basically I need something catchy to give to potential clients and people I meet. I do a lot of freelancing (from DJ'ing to wedding videography, but its mostly on the event side of things) so it's more-so about selling myself rather than identifying with a company. I'm starting to meet more people that I want to work with after meeting them so I'm revamping my business cards.

I'm looking for a clean and modern design- I know that's really vague but I'm fine with anything ranging from a symbol to just a fancy version of my name.

Details I need on the front:
Gerald Minsky
gerald@geraldminsky-demo.com
(555) 902-4416

On the back I'd like to have something simple like "Nice to have met you today" or "Great meeting you".

UPDATE 9/27 Noon: My apologies for not putting it up before- I'm definitely looking for full color. Doesn't have to be a rainbow but I am looking for the least amount of blank white as possible.

UPDATE 10/1: Really impressed with what I've been getting so far and I'm working on giving everyone feedback- if your design is still up then you're still in the run. Looking for something more unique and modern so please do not post something that looks like a template from Cardwell!

Target Market(s)

Mainly to give to people aged 18-35. Most of my encounters will be casual so the card should have a "young" feeling to it. I rarely do anything in the corporate world so it doesn't have to be boring. It should give the impression that I'm the one they should go to if they need what I do (again it changes every weekend so I'll probably say the "what I do" part.

Industry/Entity Type

Wedding

Requirements
Must have
• Basically the contact information listed above
Nice to have
• I really like the colors Blue, Silver, and Purple. They don't have to necessarily all be there though. I do like the look of polished metal if that makes sense.
Should not have
• A template that resembles card-well. I'm in a point in my life where I'm working a lot of different markets/areas so the card does not need to have an address or address placeholder.

```html
<!DOCTYPE html>
<html lang="en">
<head>
<meta charset="utf-8">
<title>Gerald Minsky — Business Card</title>
<link rel="stylesheet" href="https://fonts.googleapis.com/css2?family=Urbanist:wght@300;400;700;800&display=swap">
<style>
  :root {
    --backdrop: #ececec;
    --metal-light: #d9d9d9;
    --metal-mid: #bdbdbd;
    --metal-dark: #9a9a9a;
    --purple: #3a2a55;
    --purple-deep: #2a1d40;
    --green: #5f7a2e;
    --green-light: #8aa03c;
    --halftone-grey: #8d8d92;
    --blue: #1a7fa8;
    --blue-deep: #0d6a92;
    --lime: #c9cf2e;
    --lime-deep: #6e8a2a;
    --white: #ffffff;
  }
  * { box-sizing: border-box; margin: 0; padding: 0; }
  html, body {
    width: 1200px;
    height: 1000px;
    overflow: hidden;
    background: var(--backdrop);
    font-family: "Urbanist", "Century Gothic", sans-serif;
  }
  .canvas {
    position: relative;
    width: 1200px;
    height: 1000px;
  }
  .card {
    position: absolute;
    left: 250px;
    width: 700px;
    height: 400px;
    overflow: hidden;
    box-shadow: 0 10px 30px rgba(0,0,0,0.18);
  }
  .card--back { top: 50px; }
  .card--front { top: 530px; }

  .card-art {
    position: absolute;
    inset: 0;
    width: 100%;
    height: 100%;
    display: block;
  }

  .back-message {
    position: absolute;
    left: 0;
    right: 0;
    top: 168px;
    text-align: center;
    color: var(--white);
    font-weight: 700;
    font-size: 30px;
    letter-spacing: 0.5px;
  }

  .contact {
    position: absolute;
    right: 105px;
    top: 196px;
    text-align: right;
    color: var(--white);
    line-height: 1;
  }
  .contact-first {
    font-weight: 300;
    font-size: 24px;
    display: block;
  }
  .contact-last {
    font-weight: 800;
    font-size: 42px;
    display: block;
    margin-top: -2px;
  }
  .contact-email {
    font-weight: 700;
    font-size: 21px;
    display: block;
    margin-top: 10px;
    margin-right: -60px;
  }
  .contact-phone {
    font-weight: 700;
    font-size: 24px;
    display: block;
    margin-top: 14px;
  }
</style>
</head>
<body>
<main class="canvas">

  <section class="card card--back" aria-label="Card back">
    <svg class="card-art" viewBox="0 0 700 400" role="img" aria-label="Lime and green halftone dot texture">
      <defs>
        <linearGradient id="back-wash" x1="0" y1="0" x2="0" y2="1">
          <stop offset="0" stop-color="var(--lime-deep)"/>
          <stop offset="0.55" stop-color="#a3b634"/>
          <stop offset="1" stop-color="var(--lime)"/>
        </linearGradient>
      </defs>
      <rect width="700" height="400" fill="url(#back-wash)"/>
    </svg>
    <p class="back-message">Nice to have met you today</p>
  </section>

  <section class="card card--front" aria-label="Card front">
    <svg class="card-art" viewBox="0 0 700 400" aria-hidden="true">
      <defs>
        <linearGradient id="brushed-metal" x1="0" y1="0" x2="1" y2="0.3">
          <stop offset="0" stop-color="var(--metal-mid)"/>
          <stop offset="0.45" stop-color="var(--metal-light)"/>
          <stop offset="0.75" stop-color="var(--metal-mid)"/>
          <stop offset="1" stop-color="var(--metal-dark)"/>
        </linearGradient>
        <radialGradient id="purple-disc" cx="0.5" cy="0.5" r="0.5">
          <stop offset="0" stop-color="var(--purple-deep)"/>
          <stop offset="1" stop-color="var(--purple)"/>
        </radialGradient>
      </defs>
      <rect class="metal-base" width="700" height="400" fill="url(#brushed-metal)"/>
      <polygon class="grey-wedge" points="120,0 470,0 520,400 170,400" fill="var(--halftone-grey)" opacity="0.75"/>
      <polygon class="grey-wedge-light" points="420,270 700,400 470,400" fill="#c8c8cc" opacity="0.8"/>
      <ellipse class="green-disc" cx="300" cy="-40" rx="360" ry="170" fill="var(--green)"/>
      <ellipse class="green-disc-edge" cx="560" cy="60" rx="150" ry="120" fill="var(--green-light)" opacity="0.7"/>
      <circle class="purple-disc" cx="60" cy="330" r="230" fill="url(#purple-disc)"/>
      <circle class="blue-disc" cx="480" cy="240" r="160" fill="var(--blue)" opacity="0.95"/>
    </svg>
    <div class="contact">
      <span class="contact-first">Gerald</span>
      <span class="contact-last">Minsky</span>
      <span class="contact-email">gerald@geraldminsky-demo.com</span>
      <span class="contact-phone">(555) 902-4416</span>
    </div>
  </section>

</main>
</body>
</html>
```